Wine Bottle Label Logo Design

My fiancé and I are getting married in September and we made homemade wine which will be given to the guests as a wedding favor. We need label/logo for our wine bottles. We were looking for something rustic yet modern and simple. We had an idea for beige and cranberry colored wine stained, weathered, imperfect heart. Things that will need to be incorporated into the label design are as follows:
Our last name and also the name of the wine: Fusaldi
The year: 2012
Where is says Alcohol Content on a wine bottle normally write: Alcohol: Deceiving% by vol.
Type of wine: Red Wine
Incorporate our wedding date: Foot Stomped and Bottled for Nadia and Gus's Wedding Day 9/28/13
Wedding

```html
<!DOCTYPE html>
<html lang="en">
<head>
<meta charset="utf-8">
<title>Fusaldi Wedding Wine Label</title>
<link rel="stylesheet" href="https://fonts.googleapis.com/css2?family=Dancing+Script:wght@500;600&display=swap">
<style>
  :root {
    --paper: #ffffff;
    --bottle: #8c1414;
    --bottle-edge: #b25c5c;
    --gold-light: #f3dfa6;
    --gold-mid: #dcb874;
    --gold-deep: #c08d4c;
    --frame: #efe2b4;
    --cranberry: #d42222;
    --wine-ink: #741a12;
    --amp: #e0562a;
    --couple-grey: #a9a9a9;
    --couple-skin: #e6bfb2;
    --couple-dark: #141414;
  }
  html, body {
    margin: 0;
    padding: 0;
    overflow: hidden;
    background: var(--paper);
  }
  .canvas {
    position: relative;
    width: 1200px;
    height: 856px;
    overflow: hidden;
    background: var(--paper);
    font-family: "Dancing Script", cursive;
  }
  .bottle {
    position: absolute;
    left: 110px;
    top: 14px;
    width: 412px;
    height: 828px;
  }
  .label {
    position: absolute;
    left: 32px;
    top: 333px;
    width: 1118px;
    height: 222px;
    box-sizing: border-box;
    border: 5px solid var(--frame);
    border-radius: 12px;
    background:
      radial-gradient(ellipse at 45% 40%, rgba(255,240,200,0.55), transparent 60%),
      linear-gradient(100deg, var(--gold-deep) 0%, var(--gold-mid) 35%, var(--gold-light) 62%, var(--gold-mid) 100%);
    box-shadow: 0 2px 4px rgba(120, 80, 30, 0.35);
  }
  .couple {
    position: absolute;
    left: 75px;
    top: 250px;
    width: 385px;
    height: 295px;
    border-radius: 140px 140px 0 0;
    background: linear-gradient(180deg, var(--couple-grey) 0%, var(--couple-skin) 55%, var(--couple-dark) 100%);
    opacity: 0.9;
  }
  .couple-names {
    position: absolute;
    left: 183px;
    top: 502px;
    margin: 0;
    font-size: 27px;
    font-weight: 500;
    color: var(--cranberry);
    white-space: nowrap;
  }
  .couple-names .amp { color: var(--amp); margin: 0 10px; }
  .label-text {
    position: absolute;
    left: 500px;
    top: 350px;
    width: 610px;
    text-align: center;
    color: var(--wine-ink);
  }
  .wine-name {
    margin: 0;
    font-size: 32px;
    font-weight: 500;
    letter-spacing: 2px;
    color: var(--cranberry);
    line-height: 44px;
  }
  .dedication {
    margin: 0;
    font-size: 31px;
    font-weight: 600;
    line-height: 50px;
  }
  .details {
    margin: 4px 0 0;
    font-size: 17px;
    font-weight: 600;
    white-space: nowrap;
  }
  .details span + span { margin-left: 12px; }
  .flourish {
    position: absolute;
    top: 428px;
    width: 82px;
    height: 20px;
    border-radius: 10px;
    background: linear-gradient(90deg, transparent, rgba(116, 26, 18, 0.45), transparent);
  }
  .flourish--left { left: 500px; }
  .flourish--right { left: 1023px; }
</style>
</head>
<body>
<main class="canvas">
  <svg class="bottle" viewBox="0 0 412 828" role="img" aria-label="Red wine bottle body">
    <rect x="0" y="0" width="412" height="828" rx="40" fill="var(--bottle-edge)"/>
    <rect x="40" y="0" width="360" height="828" rx="30" fill="var(--bottle)"/>
  </svg>

  <section class="label">
  </section>

  <div class="couple" role="img" aria-label="Drawing of the bride and groom sharing a kiss"></div>
  <p class="couple-names">Gus<span class="amp">&amp;</span>Nadia</p>

  <span class="flourish flourish--left" role="img" aria-label="Decorative flourish"></span>
  <span class="flourish flourish--right" role="img" aria-label="Decorative flourish"></span>

  <div class="label-text">
    <h1 class="wine-name">FUSALDI</h1>
    <p class="dedication">Foot Stomped an bottled<br>for wedding day 28/9/13</p>
    <p class="details">
      <span>Type of wine : Red Wine</span>
      <span>Alcohol : Deceiving % by vol.</span>
      <span>The year: 2012</span>
    </p>
  </div>
</main>
</body>
</html>
```